Design the Keystone HR business card for my new business

I've just had a logo designed (attached) for my new business doing HR consulting. I'm a one person operation at this stage, my aim is to provide support and help to small to medium sized businesses with their people objectives or issues.

I'm not really into anything overly flashy, I'm not a PR or marketing agency. I'd like my card to look modern, professional and not gimmicky.

I'm thinking black front (to go with logo), double sided with details on the back, maybe in a different colour?

Logo attached in several different formats.

Front of the card to have logo and added text: People and Development Solutions

Back of the card to also feature logo in some way and say:
Megan Tulloch
PO Box (TBA)
Marrowvale QLD 4391
0438 512 976
megan@keystonehr.com.au
www.keystonehr.com.au

Target Market(s)

Small to medium businesses / business owners.

Industry/Entity Type

Marketing

Requirements
Must have
• Double sided business card.
Should not have
• Anything overly gimmicky.

```html
<!DOCTYPE html>
<html lang="en">
<head>
<meta charset="utf-8">
<title>Keystone HR — Business Card</title>
<link href="https://fonts.googleapis.com/css2?family=Raleway:wght@200;300;400&display=swap" rel="stylesheet">
<style>
  :root {
    --backdrop: #eeeeee;
    --card-black: #050505;
    --white: #f4f4f4;
    --soft-white: #d8d8d8;
    --violet: #9b6cc4;
    --violet-deep: #6a3d96;
    --rule: #8a8a8a;
  }
  * { margin: 0; padding: 0; box-sizing: border-box; }
  html, body {
    width: 1200px; height: 562px; overflow: hidden;
    background: var(--backdrop);
    font-family: "Raleway", Arial, sans-serif;
  }
  .canvas { position: relative; width: 1200px; height: 562px; }
  .card {
    position: absolute;
    background: var(--card-black);
    border-radius: 12px;
  }
  .card--front { left: 35px; top: 95px; width: 533px; height: 352px; }
  .card--back  { left: 620px; top: 95px; width: 547px; height: 356px; }

  /* Front */
  .brand-mark {
    position: absolute; left: 40px; top: 98px;
    width: 122px; height: 122px;
    border: 2px solid var(--violet); border-radius: 50%;
  }
  .brand-name {
    position: absolute; left: 185px; top: 112px;
    color: var(--white); font-weight: 300; line-height: 1;
  }
  .brand-name__main { display: block; font-size: 58px; letter-spacing: -0.5px; }
  .brand-name__sub { display: block; font-size: 31px; margin-top: 10px; margin-left: 4px; }
  .tagline {
    position: absolute; left: 190px; top: 233px;
    color: var(--violet); font-size: 14.5px; font-weight: 300;
    letter-spacing: 0.3px; text-transform: uppercase;
  }

  /* Back */
  .email {
    position: absolute; left: 50px; top: 55px;
    color: var(--violet); font-size: 18px; font-weight: 300;
    letter-spacing: 3.2px;
  }
  .back-mark {
    position: absolute; left: 413px; top: 42px;
    width: 92px; height: 92px;
    border: 2px solid var(--violet-deep); border-radius: 50%;
    display: flex; align-items: center; justify-content: center;
    color: var(--violet); font-size: 12px; font-weight: 300; letter-spacing: 0.5px;
  }
  .person-name {
    position: absolute; left: 50px; top: 188px;
    color: var(--white); font-size: 23px; font-weight: 300;
    letter-spacing: 0.5px; text-transform: uppercase;
  }
  .name-rule {
    position: absolute; left: 40px; top: 218px;
    width: 468px; height: 1px; background: var(--rule);
  }
  .contact {
    position: absolute; left: 50px; top: 245px;
    list-style: none;
    color: var(--soft-white); font-size: 15px; font-weight: 400; line-height: 21px;
  }
</style>
</head>
<body>
<main class="canvas">
  <section class="card card--front" aria-label="Card front">
    <div class="brand-mark" aria-hidden="true"></div>
    <h1 class="brand-name">
      <span class="brand-name__main">Keystone</span>
      <span class="brand-name__sub">HR Consulting</span>
    </h1>
    <p class="tagline">People and Development Solutions</p>
  </section>

  <section class="card card--back" aria-label="Card back">
    <p class="email">megan@keystonehr.com.au</p>
    <div class="back-mark">Keystone HR</div>
    <h2 class="person-name">Megan Tulloch</h2>
    <div class="name-rule"></div>
    <ul class="contact">
      <li>PO Box (TBA)</li>
      <li>Marrowvale QLD 4391</li>
      <li>0438 512 976</li>
    </ul>
  </section>
</main>
</body>
</html>
```